Broadcaster,Conference Host,Facilitator

Looking for a business card and logo to create the Grant Felber brand .. Something with a slant towards radio and conference speaking
I like the idea of classic black white or grey but open to suggestions

Target Market(s)

Corporates

Industry/Entity Type

Business

Contact Information for Business Card

Grant Felber
Email : Grant.Felber@quorvamail.co.uk
Mobile : +44 7700 382046
Chirpline : @Grantfelber

Font styles to use
Serif
Decorative
Script

Requirements
Must have
• Feel classy and dynamic
Should not have
• Cartoons

```html
<!DOCTYPE html>
<html lang="en">
<head>
<meta charset="utf-8">
<title>Grant Felber business card</title>
<link href="https://fonts.googleapis.com/css2?family=Dosis:wght@500&display=swap" rel="stylesheet">
<style>
  :root {
    --backdrop: #3aa9bb;
    --card-front: #ffffff;
    --card-back: #9a9a9a;
    --ink: #1b1b1b;
  }
  * { margin: 0; padding: 0; box-sizing: border-box; }
  html, body {
    width: 1200px; height: 852px; overflow: hidden;
    background: var(--backdrop);
  }
  .canvas { position: relative; width: 1200px; height: 852px; }
  .card {
    position: absolute; left: 374px; width: 448px; height: 273px;
    border-radius: 16px;
  }
  .card--front { top: 123px; background: var(--card-front); }
  .card--back { top: 457px; background: var(--card-back); }
  .wordmark {
    position: absolute; display: flex; align-items: center; gap: 7px;
    font-family: "Dosis", sans-serif; font-weight: 500;
    font-size: 27px; color: var(--ink); letter-spacing: 0.5px;
    line-height: 1; white-space: nowrap;
  }
  .wordmark__dot {
    width: 14px; height: 14px; border-radius: 50%;
    background: var(--ink); flex: none;
  }
  .card--front .wordmark { right: 26px; top: 95px; }
  .card--back .wordmark { left: 50%; top: 133px; transform: translateX(-50%); }
  .contact {
    position: absolute; right: 26px; top: 185px;
    list-style: none;
    font-family: "Dosis", sans-serif; font-weight: 500;
    font-size: 14.5px; letter-spacing: 1px; color: var(--ink);
  }
  .contact__item {
    display: flex; justify-content: flex-end; align-items: center;
    gap: 9px; height: 21.5px;
  }
  .contact__icon { width: 16px; height: 16px; flex: none; }
</style>
</head>
<body>
<main class="canvas">
  <section class="card card--front" aria-label="Card front">
    <div class="wordmark"><span class="wordmark__dot"></span>Grant Felber</div>
    <ul class="contact">
      <li class="contact__item">Email : Grant.Felber@quorvamail.co.uk
        <svg class="contact__icon" viewBox="0 0 16 16" aria-hidden="true">
          <rect x="1" y="3.5" width="14" height="9.5" rx="1" fill="#1b1b1b"/>
          <path d="M1.5 4.5 8 9.2 14.5 4.5" fill="none" stroke="#fff" stroke-width="1.2"/>
        </svg>
      </li>
      <li class="contact__item">Mobile : +44 7700 382046
        <svg class="contact__icon" viewBox="0 0 16 16" aria-hidden="true">
          <rect x="3.5" y="0.8" width="9" height="14.4" rx="1.8" fill="none" stroke="#1b1b1b" stroke-width="1.2"/>
          <line x1="4" y1="3" x2="12" y2="3" stroke="#1b1b1b" stroke-width="0.9"/>
          <line x1="4" y1="12.4" x2="12" y2="12.4" stroke="#1b1b1b" stroke-width="0.9"/>
        </svg>
      </li>
      <li class="contact__item">Chirpline : @Grantfelber
        <svg class="contact__icon" viewBox="0 0 16 16" aria-hidden="true">
          <circle cx="8" cy="8" r="6" fill="#1b1b1b"/>
        </svg>
      </li>
    </ul>
  </section>
  <section class="card card--back" aria-label="Card back">
    <div class="wordmark"><span class="wordmark__dot"></span>Grant Felber</div>
  </section>
</main>
</body>
</html>
```